Liam Kovac Fitness Business Card

I Need a really cool and creative yet modern and cutting edge. I run a personal training company, I have a logo already which ill submit images of. Id like the base colors to be black and white with a little red as a highlight color. Charcoal grey is fine also. My clientele is mostly comprised of young professionals who are in touch with modern culture art and are interested in "cool" so if there was one thing i want this business card to be it sexy and cool.

Target Market(s)

young professionals who are image conscious, care about their health, looking and feeling good. They know what is cool and expect the best.

Industry/Entity Type

Training

Requirements
Must have
• - must be a 2 sided card
- must include the following:

Liam Kovac CPT
646 392 7105
Liam@LiamKovacFitness.example
www.LiamKovacFitness.example
Nice to have
• id like to see some unconventional shape ideas as well as conventional ones

```html
<!DOCTYPE html>
<html lang="en">
<head>
<meta charset="utf-8">
<title>Liam Kovac Fitness – Business Card</title>
<link rel="stylesheet" href="https://fonts.googleapis.com/css2?family=Jost:wght@300;400;500&display=swap">
<style>
  :root {
    --ink: #1f1f1f;
    --charcoal: #262626;
    --paper: #ffffff;
    --accent: #e8242b;
    --backdrop-light: #c9c9c9;
    --backdrop-dark: #5a5a5a;
    --muted: #2b2b2b;
  }
  * { box-sizing: border-box; margin: 0; padding: 0; }
  html, body { width: 1200px; height: 900px; overflow: hidden; }
  body {
    position: relative;
    font-family: "Jost", sans-serif;
    background: radial-gradient(ellipse at 55% 40%, var(--backdrop-light) 0%, #9a9a9a 55%, var(--backdrop-dark) 100%);
  }
  .card {
    position: absolute;
    width: 700px;
    height: 400px;
    overflow: hidden;
    box-shadow: 0 18px 40px rgba(0,0,0,.35);
  }

  /* Contact side */
  .card--contact { left: 110px; top: 50px; background: var(--paper); }
  .contact__band {
    height: 130px;
    background: var(--ink);
    display: flex;
    align-items: flex-end;
    justify-content: center;
    padding: 0 0 22px 120px;
  }
  .brand {
    display: flex;
    align-items: center;
    gap: 12px;
    color: var(--paper);
    font-weight: 400;
  }
  .brand__mark { width: 12px; height: 12px; background: var(--accent); }
  .contact__band .brand { font-size: 30px; letter-spacing: .5px; }
  .contact__body { padding: 38px 40px 0; }
  .person__name, .person__title {
    font-size: 30px;
    font-weight: 500;
    color: var(--muted);
    line-height: 1.2;
  }
  .person__rule {
    width: 380px;
    height: 2px;
    background: var(--accent);
    margin: 16px 0 22px -40px;
  }
  .details { list-style: none; }
  .details li {
    display: flex;
    align-items: center;
    gap: 22px;
    font-size: 24px;
    font-weight: 500;
    color: var(--muted);
    line-height: 1.4;
  }
  .details svg { width: 16px; height: 16px; flex: none; fill: var(--muted); }

  /* Brand side */
  .card--brand {
    left: 390px; top: 450px;
    background: linear-gradient(160deg, #1a1a1a 0%, var(--charcoal) 60%, #333 100%);
    display: flex;
    flex-direction: column;
    align-items: center;
    justify-content: center;
  }
  .card--brand .brand { font-size: 52px; font-weight: 300; gap: 18px; }
  .card--brand .brand__mark { width: 18px; height: 18px; border-radius: 50%; }
  .tagline {
    margin-top: 14px;
    align-self: flex-end;
    margin-right: 120px;
    font-size: 20px;
    font-weight: 300;
    color: var(--paper);
    letter-spacing: .5px;
  }
</style>
</head>
<body>

  <section class="card card--contact" aria-label="Card contact side">
    <header class="contact__band">
      <div class="brand"><span class="brand__mark"></span><span>Liam Kovac Fitness</span></div>
    </header>
    <div class="contact__body">
      <p class="person__name">Liam Kovac</p>
      <p class="person__title">CPT</p>
      <div class="person__rule"></div>
      <ul class="details">
        <li>
          <svg viewBox="0 0 16 16" aria-hidden="true"><path d="M4 1l2.5 3-1.5 1.5c.8 2 2.5 3.7 4.5 4.5L11 8.5l3 2.5-1.5 2.5C8 14 2 8 2.5 2.5z"/></svg>
          646 392 7105
        </li>
        <li>
          <svg viewBox="0 0 16 16" aria-hidden="true"><path d="M1 3h14v10H1z M1 3l7 6 7-6" fill="none" stroke="#2b2b2b" stroke-width="1.6"/><path d="M1 3h14L8 9z"/></svg>
          Liam@LiamKovacFitness.example
        </li>
        <li>
          <svg viewBox="0 0 16 16" aria-hidden="true"><circle cx="8" cy="8" r="7"/><path d="M1 8h14M8 1v14M3 4.5h10M3 11.5h10" stroke="#fff" stroke-width="1"/><ellipse cx="8" cy="8" rx="3" ry="7" fill="none" stroke="#fff" stroke-width="1"/></svg>
          www.LiamKovacFitness.example
        </li>
      </ul>
    </div>
  </section>

  <section class="card card--brand" aria-label="Card brand side">
    <div class="brand"><span class="brand__mark"></span><span>Liam Kovac Fitness</span></div>
    <p class="tagline">Stronger every day</p>
  </section>

</body>
</html>
```